I need a box design created for a DNA Fitness Test

I need a modern and sleek box design for a fitness test. The box needs to have our logo on it and should be clean and modern. The Box is 9 Inches Long 3 and 3/4 inches wide, and 2 inches tall. Company logo attached. The company name is corvane wellness.

Target Market(s)

Fitness

Industry/Entity Type

Fitness

Requirements
Must have
• Our logo

```html
<!DOCTYPE html>
<html lang="en">
<head>
<meta charset="utf-8">
<title>Corvane Wellness – DNA Fitness Test Box</title>
<link rel="stylesheet" href="https://fonts.googleapis.com/css2?family=Montserrat:wght@800&family=Arimo:ital,wght@0,400;0,700;1,400&display=swap">
<style>
  :root {
    --ink: #0b0b0b;
    --brand-blue: #0d4fa3;
    --band-blue: #2a78b5;
    --band-teal: #3aae9a;
    --band-green: #8cc64a;
    --fold-grey: #c4c4c4;
    --paper: #ffffff;
    --frame: #222222;
  }
  * { box-sizing: border-box; margin: 0; padding: 0; }
  html, body { width: 923px; height: 1200px; overflow: hidden; background: var(--paper); }
  .box-panel { position: relative; width: 923px; height: 1200px; }
  .backdrop { position: absolute; inset: 0; }
  .frame { position: absolute; left: 34px; top: 33px; width: 854px; height: 1133px; border: 1px solid var(--frame); }

  .wordmark { position: absolute; text-align: center;
    font-family: "Montserrat", Arial, sans-serif; font-weight: 800; color: var(--ink); line-height: 1; }
  .wordmark .name { display: block; }
  .wordmark .sub { display: block; letter-spacing: 0.55em; padding-left: 0.55em; }
  .wordmark--flipped { top: 80px; left: 362px; width: 200px; transform: rotate(180deg); }
  .wordmark--flipped .name { font-size: 22px; }
  .wordmark--flipped .sub { font-size: 8px; margin-top: 3px; }
  .wordmark--main { top: 432px; left: 252px; width: 400px; }
  .wordmark--main .name { font-size: 52px; }
  .wordmark--main .sub { font-size: 20px; margin-top: 9px; }
  .wordmark--small { top: 687px; left: 362px; width: 200px; }
  .wordmark--small .name { font-size: 22px; }
  .wordmark--small .sub { font-size: 8px; margin-top: 3px; }
  .brand-dot { position: absolute; border-radius: 50%; background: var(--ink); }
  .brand-dot--main { left: 427px; top: 330px; width: 52px; height: 52px; }

  .pitch { position: absolute; left: 70px; top: 808px; width: 520px; font-family: "Arimo", Arial, sans-serif; color: var(--brand-blue); }
  .pitch h2 { font-size: 27px; font-weight: 700; letter-spacing: 0.01em; line-height: 1; }
  .pitch .lead { font-size: 15px; line-height: 18.5px; margin-top: 8px; white-space: nowrap; }
  .benefits { display: grid; grid-template-columns: 281px 220px; margin-top: 23px; list-style: none; font-size: 15px; font-style: italic; line-height: 18.5px; white-space: nowrap; }
  .benefits li::before { content: "•"; font-style: normal; margin-right: 7px; }
  .pitch .closing { font-size: 15px; margin-top: 27px; }
</style>
</head>
<body>
<div class="box-panel">
  <svg class="backdrop" width="923" height="1200" viewBox="0 0 923 1200">
    <defs>
      <linearGradient id="foldLeft" x1="0" y1="0" x2="1" y2="0.35">
        <stop offset="0" stop-color="var(--fold-grey)"/>
        <stop offset="0.9" stop-color="#ffffff" stop-opacity="0"/>
      </linearGradient>
      <linearGradient id="foldRight" x1="1" y1="1" x2="0.2" y2="0">
        <stop offset="0" stop-color="#bdbdbd"/>
        <stop offset="1" stop-color="#ffffff" stop-opacity="0"/>
      </linearGradient>
      <linearGradient id="fadeDown" x1="0" y1="0" x2="0" y2="1">
        <stop offset="0" stop-color="#ffffff" stop-opacity="0"/>
        <stop offset="1" stop-color="#ffffff"/>
      </linearGradient>
      <linearGradient id="band" x1="0" y1="0" x2="1" y2="1">
        <stop offset="0" stop-color="var(--band-blue)"/>
        <stop offset="0.55" stop-color="var(--band-teal)"/>
        <stop offset="1" stop-color="var(--band-green)"/>
      </linearGradient>
      <linearGradient id="photo" x1="0" y1="0" x2="0" y2="1">
        <stop offset="0" stop-color="#eef5dc"/>
        <stop offset="0.55" stop-color="#7fb886"/>
        <stop offset="1" stop-color="#1a5a5e"/>
      </linearGradient>
    </defs>
    <polygon points="34,300 420,800 34,800" fill="url(#foldLeft)"/>
    <polygon points="34,108 82,105 285,360 34,240" fill="url(#foldLeft)"/>
    <rect x="34" y="660" width="420" height="145" fill="url(#fadeDown)"/>
    <polygon points="527,160 888,560 888,620 760,520" fill="url(#foldRight)"/>
    <polygon points="34,33 175,33 338,300 290,300 34,110" fill="url(#band)" role="img" aria-label="Decorative blue-to-green geometric pattern"/>
    <polygon points="606,466 660,470 888,600 888,872" fill="url(#band)" role="img" aria-label="Decorative blue-to-green geometric pattern"/>
    <rect x="553" y="812" width="308" height="354" fill="url(#photo)" role="img" aria-label="Photo of a smiling fit man and woman standing back to back with arms crossed"/>
    <polygon points="402,1166 800,1040 700,1166" fill="url(#band)" role="img" aria-label="Decorative blue-to-green geometric pattern"/>
  </svg>
  <div class="frame"></div>

  <div class="wordmark wordmark--flipped"><span class="name">CORVANE</span><span class="sub">WELLNESS</span></div>
  <div class="brand-dot brand-dot--main"></div>
  <div class="wordmark wordmark--main"><span class="name">CORVANE</span><span class="sub">WELLNESS</span></div>
  <div class="wordmark wordmark--small"><span class="name">CORVANE</span><span class="sub">WELLNESS</span></div>

  <section class="pitch">
    <h2>UNLOCK YOUR POTENTIAL</h2>
    <p class="lead">Our team od scientists have spent years using the latest scientific<br>research and the latest technology to develop our Corvane Wellness line<br>of products. By using a simple and painless cheek swab we are able to<br>reveal the details about an individual's unique fitness and nutrition<br>requirements, unlocking their body's true potential for success.</p>
    <ul class="benefits">
      <li>Leverage impulsive tendencies</li>
      <li>Mainain weight loss</li>
      <li>Learn to stop eating when full</li>
      <li>Recover Faster</li>
      <li>Train your body to burn fat effectively</li>
    </ul>
    <p class="closing">Get all of this and more from Corvane Wellness.</p>
  </section>
</div>
</body>
</html>
```